Flyer-Design für Hotel mit Halbpension
Obwohl ich keine Ahnung hatte von Design hat Sie mir wirklich gut mit Allem geholfen. Sehr schnell Service bei jeder Frage. Vielen Dank
Zielgruppe
Hotel /Restaurant
Aufgabenstellung
Wir haben bis jetzt nur Halbpension für unsere Hausgäste gemacht, aber wir möchten dass ab Ostern auch gerne für andere Gäste machen.
Unsere Spezialitäten sind Schmorgerichte und Spareribs.
Alles für ein fester Preis: 3-Gänge 18,90, 2 Gänge 15,90, 1 Gang 12,90.
Jeden Sonntag soll es auserdem Schnitzeltag sein: € 6,99 für ein Schnitzel mit Pommer und Salat. Sauce € 1,00 extra.
Folgende Texte sollen in den Flyer:
Vorderseite:
Neu in Manderscheid:
Restaurant im Hotel am Birkenhain
Ab Ostern bis Ende Oktober.
Probieren Sie unsere Spezialitäten:
Schmorgerichte
Ofengerichte (Fisch, FIeisch, Vegetarisch)
Schnitzel
Spare-ribs
Geöffnet von 18:30 bis 20:00 Uhr.
Montag und Dienstag nur Hausgäste.
Rückseite:
Unser Sonderangebot am Sonntag
Von 12:00 bis 20:00 Uhr.
Schweineschnitzel 'Wiener Art' 200 Gr. mit Pommes und Salat.
Pro Perzon: € 6,99
Extra Div. Saucen: € 2,00 Aufpreis

```html
<!DOCTYPE html>
<html lang="de">
<head>
<meta charset="utf-8">
<title>Flyer – Restaurant im Hotel am Birkenhain</title>
<link href="https://fonts.googleapis.com/css2?family=Oswald:wght@300;400;500&display=swap" rel="stylesheet">
<style>
  :root{
    --green:#4caf3a;
    --green-dark:#3d9a2d;
    --ink:#222;
    --footer:#2b2d2c;
    --footer-text:#d8d8d8;
    --bg:#d9d9d9;
    --paper:#ffffff;
  }
  *{box-sizing:border-box;margin:0;padding:0}
  html,body{width:1200px;height:2770px;overflow:hidden}
  body{background:linear-gradient(135deg,#e6e6e6,#c9c9c9);font-family:"Oswald",sans-serif;position:relative}
  .flyer{position:absolute;left:180px;top:765px;width:840px;height:1240px;background:var(--paper);overflow:hidden;box-shadow:0 6px 24px rgba(0,0,0,.2)}
  .top-rule{position:absolute;left:0;top:0;width:100%;height:9px;background:var(--green)}
  .hotel-photo{position:absolute;left:28px;top:22px;width:784px;height:362px;border-radius:0 0 0 40px;
    background:linear-gradient(180deg,#9cc3e6 0%,#d7e4ee 30%,#e9e7e1 55%,#b9b6ad 75%,#6f8f55 100%)}
  .headline-tag{position:absolute;left:38px;top:38px;background:var(--green);color:#fff;font-size:36px;font-weight:400;padding:4px 16px;transform:rotate(-3deg);letter-spacing:.5px}
  .sunday-badge{position:absolute;left:650px;top:218px;width:190px;height:190px}
  .sunday-badge svg{position:absolute;inset:0}
  .sunday-text{position:absolute;inset:0;display:flex;flex-direction:column;align-items:center;justify-content:center;color:#fff;text-align:center;padding:0 26px}
  .sunday-title{font-size:22px;line-height:1.05}
  .sunday-desc{font-size:11.5px;font-weight:300;line-height:1.3;margin-top:6px}
  .price-dark{position:absolute;left:598px;top:245px;width:66px;height:66px;border-radius:50%;background:#2b2b2b;color:#fff;display:flex;flex-direction:column;align-items:center;justify-content:center;font-size:17px;line-height:1}
  .price-dark small,.price-star small{font-size:9px;font-weight:300}
  .section-title{position:absolute;left:28px;top:408px;width:784px;display:flex;align-items:center;gap:18px;color:var(--green);font-size:48px;font-weight:400}
  .section-title::before,.section-title::after{content:"";flex:1;height:2px;background:var(--green)}
  .section-sub{position:absolute;left:0;top:485px;width:100%;text-align:center;font-size:19px;color:var(--ink);font-weight:400}
  .menu-col{position:absolute;top:540px;width:228px}
  .menu-col h3{font-size:24px;font-weight:400;color:var(--green);text-align:center;height:40px}
  .menu-photo{width:228px;height:150px;border-radius:14px;box-shadow:0 3px 8px rgba(0,0,0,.35);border:3px solid #fff}
  .photo-salad{background:linear-gradient(135deg,#3a4a3a,#8a5a35 45%,#5a2e4a 100%)}
  .photo-ribs{background:linear-gradient(135deg,#2c3a2a,#7a3a1e 50%,#3a2a20 100%)}
  .photo-plate{background:linear-gradient(135deg,#5a3520,#9a4a3a 45%,#c04468 70%,#4a2e22)}
  .price-star{position:absolute;right:-22px;top:16px;width:68px;height:68px}
  .price-star svg{position:absolute;inset:0}
  .price-star span{position:absolute;inset:0;display:flex;flex-direction:column;align-items:center;justify-content:center;color:#fff;font-size:17px;line-height:1}
  .castle-photo{position:absolute;left:0;top:740px;width:840px;height:412px;
    background:linear-gradient(180deg,rgba(255,255,255,1) 0%,rgba(255,255,255,0) 12%),linear-gradient(160deg,#5e8f3e 0%,#3f6e2c 45%,#7a7a6a 60%,#2f5a24 100%)}
  .specials-note{position:absolute;left:45px;top:780px;width:265px;height:320px;background:linear-gradient(180deg,#fafafa,#e9e9e9);box-shadow:3px 4px 10px rgba(0,0,0,.35);text-align:center;padding-top:30px}
  .note-marker{position:absolute;left:-2px;top:12px;width:14px;height:60px;background:var(--green)}
  .note-title{color:var(--green);font-size:18px;line-height:1.25;font-weight:400}
  .note-rule{width:80px;height:1px;background:#999;margin:14px auto 12px}
  .note-list{list-style:none;color:var(--ink);font-size:18px;font-weight:400}
  .note-list li{margin-bottom:18px;line-height:1.15}
  .note-list small{display:block;font-size:12px;font-weight:300}
  .hours-strip{position:absolute;left:0;top:1112px;width:840px;height:38px;background:rgba(76,175,58,.85);color:#fff;text-align:center;font-size:15px;line-height:38px;font-weight:300}
  .footer{position:absolute;left:0;top:1150px;width:840px;height:90px;background:var(--footer);color:var(--footer-text);font-size:15px;font-weight:300}
  .contact{position:absolute;top:18px;display:flex;gap:10px;line-height:1.6}
  .contact svg{width:16px;height:16px;flex:none;margin-top:4px;fill:var(--footer-text)}
  .contact-row{display:flex;gap:10px;align-items:flex-start}
</style>
</head>
<body>
<main class="flyer">
  <div class="top-rule"></div>
  <div class="hotel-photo" role="img" aria-label="Foto der Hotelfassade mit Terrasse und Sonnenschirm unter blauem Himmel"></div>
  <div class="headline-tag">NEU IN MANDERSCHEID</div>

  <div class="price-dark"><small>je</small>6,90€</div>
  <div class="sunday-badge">
    <svg viewBox="0 0 170 170"><polygon fill="#4caf3a" points="165,85 150.7,102.6 154.3,125 133.1,133.1 125,154.3 102.6,150.7 85,165 67.4,150.7 45,154.3 36.9,133.1 15.7,125 19.3,102.6 5,85 19.3,67.4 15.7,45 36.9,36.9 45,15.7 67.4,19.3 85,5 102.6,19.3 125,15.7 133.1,36.9 154.3,45 150.7,67.4"/></svg>
    <div class="sunday-text">
      <div class="sunday-title">SONNTAG IST<br>SCHNITZELTAG</div>
      <div class="sunday-desc">Schweineschnitzel<br>„Wiener Art“ 200gr<br>mit Pommes und Salat</div>
    </div>
  </div>

  <h2 class="section-title">UNSERE SPEZIALITÄTEN</h2>
  <p class="section-sub">alle Speisen als 1-Gang Menü, 2-Gänge Menü oder 3-Gänge Menü zum Festpreis erhältlich.</p>

  <section class="menu-col" style="left:28px">
    <h3>1-GANG MENÜS</h3>
    <div class="menu-photo photo-salad" role="img" aria-label="Foto bunter Salatschalen mit Gemüse"></div>
    <div class="price-star"><svg viewBox="0 0 170 170"><polygon fill="#4caf3a" points="165,85 150.7,102.6 154.3,125 133.1,133.1 125,154.3 102.6,150.7 85,165 67.4,150.7 45,154.3 36.9,133.1 15.7,125 19.3,102.6 5,85 19.3,67.4 15.7,45 36.9,36.9 45,15.7 67.4,19.3 85,5 102.6,19.3 125,15.7 133.1,36.9 154.3,45 150.7,67.4"/></svg><span><small>je</small>12,90€</span></div>
  </section>
  <section class="menu-col" style="left:295px">
    <h3>2-GÄNGE MENÜS</h3>
    <div class="menu-photo photo-ribs" role="img" aria-label="Foto gegrillter Spare Ribs auf einem Brett"></div>
    <div class="price-star"><svg viewBox="0 0 170 170"><polygon fill="#4caf3a" points="165,85 150.7,102.6 154.3,125 133.1,133.1 125,154.3 102.6,150.7 85,165 67.4,150.7 45,154.3 36.9,133.1 15.7,125 19.3,102.6 5,85 19.3,67.4 15.7,45 36.9,36.9 45,15.7 67.4,19.3 85,5 102.6,19.3 125,15.7 133.1,36.9 154.3,45 150.7,67.4"/></svg><span><small>je</small>15,90€</span></div>
  </section>
  <section class="menu-col" style="left:564px">
    <h3>3-GÄNGE MENÜS</h3>
    <div class="menu-photo photo-plate" role="img" aria-label="Foto eines angerichteten Tellers mit Schmorgericht"></div>
    <div class="price-star"><svg viewBox="0 0 170 170"><polygon fill="#4caf3a" points="165,85 150.7,102.6 154.3,125 133.1,133.1 125,154.3 102.6,150.7 85,165 67.4,150.7 45,154.3 36.9,133.1 15.7,125 19.3,102.6 5,85 19.3,67.4 15.7,45 36.9,36.9 45,15.7 67.4,19.3 85,5 102.6,19.3 125,15.7 133.1,36.9 154.3,45 150.7,67.4"/></svg><span><small>je</small>18,90€</span></div>
  </section>

  <div class="castle-photo" role="img" aria-label="Landschaftsfoto bewaldeter Hügel mit Burgruine"></div>

  <aside class="specials-note">
    <div class="note-marker"></div>
    <p class="note-title">PROBIEREN SIE<br>UNSERE SPEZIALITÄTEN</p>
    <div class="note-rule"></div>
    <ul class="note-list">
      <li>SCHMORGERICHTE</li>
      <li>OFENGERICHTE<small>(Fisch, Fleisch, Vegetarisch)</small></li>
      <li>SCHNITZEL</li>
      <li>SPARE RIBS</li>
    </ul>
  </aside>

  <div class="hours-strip">Ab Ostern bis Ende Oktober | 18:30 Uhr bis 20:00 Uhr | Montag &amp; Dienstag nur Hausgäste</div>

  <footer class="footer">
    <div class="contact" style="left:30px">
      <svg viewBox="0 0 24 24"><path d="M12 2a7 7 0 0 0-7 7c0 5 7 13 7 13s7-8 7-13a7 7 0 0 0-7-7zm0 9.5A2.5 2.5 0 1 1 12 6.5a2.5 2.5 0 0 1 0 5z"/></svg>
      <div>Hotel am Birkenhain<br>Lindenweg 7 | 54531 Manderscheid</div>
    </div>
    <div class="contact" style="left:330px;flex-direction:column;gap:0">
      <div class="contact-row"><svg viewBox="0 0 24 24"><path d="M6.6 10.8a15 15 0 0 0 6.6 6.6l2.2-2.2a1 1 0 0 1 1-.25 11.4 11.4 0 0 0 3.6.57 1 1 0 0 1 1 1V20a1 1 0 0 1-1 1A17 17 0 0 1 3 4a1 1 0 0 1 1-1h3.5a1 1 0 0 1 1 1c0 1.25.2 2.45.57 3.57a1 1 0 0 1-.25 1z"/></svg><span>0049 170 555 0187</span></div>
      <div class="contact-row"><svg viewBox="0 0 24 24"><path d="M3 5h18v14H3zm2 2v.5l7 4.5 7-4.5V7l-7 4.5z"/></svg><span>hotelbirkenhain@mailpost.de</span></div>
    </div>
    <div class="contact" style="left:585px">
      <svg viewBox="0 0 24 24"><path d="M12 2a10 10 0 1 0 0 20 10 10 0 0 0 0-20zm6.9 6h-3a15 15 0 0 0-1.3-3.9A8 8 0 0 1 18.9 8zM12 4c.8 1.2 1.5 2.5 1.9 4h-3.8c.4-1.5 1.1-2.8 1.9-4zM4.3 14a8 8 0 0 1 0-4h3.4a16 16 0 0 0 0 4zm.8 2h3a15 15 0 0 0 1.3 3.9A8 8 0 0 1 5.1 16zm3-8h-3a8 8 0 0 1 4.3-3.9A15 15 0 0 0 8.1 8zM12 20c-.8-1.2-1.5-2.5-1.9-4h3.8c-.4 1.5-1.1 2.8-1.9 4zm2.3-6H9.7a14 14 0 0 1 0-4h4.6a14 14 0 0 1 0 4zm.3 5.9a15 15 0 0 0 1.3-3.9h3a8 8 0 0 1-4.3 3.9zm1.7-5.9a16 16 0 0 0 0-4h3.4a8 8 0 0 1 0 4z"/></svg>
      <div>Besuchen Sie uns online:<br>www.hotelambirkenhain.com</div>
    </div>
  </footer>
</main>
</body>
</html>
```